LVR, Inc. business card design

LVR, Inc is a distributor of fragrances and cosmetics globally tht sells to retailers, wholesalers and coporations

The card design should be elegant and serious .

They recently open a state of the art facility that I would like to tie in the card design to . See pictures or go to tq7buildworks.example and view the Scent Hub of Norvania building and reception area for design ideas . the Building roof is all solar panel as well .

Brisco Market(s)

Corporations and stores like Brisco, Dun Kell

Industry/Entity Type

Business

Contact Information for Business Card

On the front
LVR, Inc.
Brand name distributors of fragrances and beauty products
On the back :

Teodor Umbrell
President
Phone (icon) 555.204.8861 ext. 101 &102
Cell ( icon) 555.719.2043
email ( icon) teodor@scent-hub.example
fax ( icon) 555.204.8870
website: www.scent-hub.example

4417 Larchmere Road
Harlow Bay, NY 11990

Font styles to use
Script

Colors
33a6d7
0492cd
ffffff
0655a3

Requirements
Must have
• Sharp design easily read and some design feature or accent of color to make it look like a beauty company very high end but also corporate.
• Need more creativity!!
• LVR,Inc. in a creative fashion
Nice to have
• Blue shades
• Would like to see some brush stroke designs for LVR incorporating silver foil
Should not have
• Faces, facial elements, perfume bottles, flowers ,
• Not to read Scent Hub of Norvania

```html
<!DOCTYPE html>
<html lang="en">
<head>
<meta charset="utf-8">
<title>LVR, Inc. – Business Card</title>
<link href="https://fonts.googleapis.com/css2?family=Open+Sans:wght@400;600&display=swap" rel="stylesheet">
<style>
  :root {
    --page-bg: #e9e6e1;
    --blue-light: #33a6d7;
    --blue-mid: #0492cd;
    --blue-deep: #0655a3;
    --panel-grey: #4a4b4d;
    --panel-grey-dark: #3c3d3f;
    --white: #ffffff;
    --logo-tint: #f3e4f0;
    --icon-bg: #d9d9d9;
    --icon-ink: #444444;
  }
  * { box-sizing: border-box; margin: 0; padding: 0; }
  html, body { width: 1200px; height: 892px; overflow: hidden; }
  body {
    background: var(--page-bg);
    font-family: "Open Sans", Arial, sans-serif;
    position: relative;
  }
  .card {
    position: absolute;
    left: 270px;
    width: 660px;
    height: 377px;
    overflow: hidden;
    background: linear-gradient(135deg, var(--blue-light) 0%, var(--blue-mid) 55%, var(--blue-deep) 130%);
    box-shadow: 0 6px 18px rgba(0,0,0,0.25);
  }
  .card--front { top: 46px; }
  .card--back { top: 469px; }
  .card__shape { position: absolute; inset: 0; }

  .brand {
    position: absolute;
    display: flex;
    align-items: center;
    gap: 12px;
    color: var(--logo-tint);
    font-weight: 600;
    white-space: nowrap;
  }
  .brand__dot {
    width: 22px; height: 22px;
    border-radius: 50%;
    background: var(--logo-tint);
    flex: none;
  }
  .card--front .brand { left: 40px; top: 160px; font-size: 34px; }
  .card--back .brand { left: 0; right: 0; top: 0; bottom: 0; justify-content: center; font-size: 48px; }

  .person {
    position: absolute;
    right: 38px;
    top: 34px;
    text-align: right;
    color: var(--white);
  }
  .person__name { font-size: 25px; font-weight: 600; letter-spacing: 0.2px; }
  .person__title { font-size: 17px; margin-top: 2px; }

  .contact {
    position: absolute;
    right: 30px;
    top: 118px;
    list-style: none;
    color: var(--white);
    font-size: 15px;
  }
  .contact__item {
    display: flex;
    justify-content: flex-end;
    align-items: center;
    gap: 14px;
    height: 27px;
  }
  .contact__icon {
    width: 14px; height: 14px;
    background: var(--icon-bg);
    display: flex; align-items: center; justify-content: center;
  }
  .contact__icon svg { width: 10px; height: 10px; }

  .address {
    position: absolute;
    left: 285px;
    bottom: 32px;
    color: var(--white);
    font-size: 17px;
    line-height: 1.45;
    font-style: normal;
  }
</style>
</head>
<body>

<section class="card card--front">
  <svg class="card__shape" viewBox="0 0 660 377" aria-hidden="true">
    <defs>
      <linearGradient id="panelShade" x1="0" y1="0" x2="1" y2="1">
        <stop offset="0" stop-color="#4a4b4d"/>
        <stop offset="1" stop-color="#3c3d3f"/>
      </linearGradient>
    </defs>
    <path d="M395 0 C335 0 330 150 290 225 C250 300 205 350 175 377 L660 377 L660 0 Z" fill="url(#panelShade)"/>
    <path d="M409 0 C349 0 344 150 304 225 C264 300 219 350 189 377" fill="none" stroke="#ffffff" stroke-width="3"/>
  </svg>

  <div class="brand"><span class="brand__dot"></span><span>LVR, Inc.</span></div>

  <div class="person">
    <p class="person__name">Teodor Umbrell</p>
    <p class="person__title">President</p>
  </div>

  <ul class="contact">
    <li class="contact__item">555.719.2043
      <span class="contact__icon"><svg viewBox="0 0 10 10"><rect x="3" y="1" width="4" height="8" rx="0.8" fill="#444"/></svg></span>
    </li>
    <li class="contact__item">555.204.8870 (101 &amp; 102)
      <span class="contact__icon"><svg viewBox="0 0 10 10"><path d="M2 2 C2 6 4 8 8 8 L8 6.5 L6.5 5.8 L5.8 6.5 C4.6 6 4 5.4 3.5 4.2 L4.2 3.5 L3.5 2 Z" fill="#444"/></svg></span>
    </li>
    <li class="contact__item">www.scent-hub.example
      <span class="contact__icon"><svg viewBox="0 0 10 10"><circle cx="5" cy="5" r="3.6" fill="none" stroke="#444" stroke-width="1"/><path d="M1.4 5 H8.6 M5 1.4 V8.6" stroke="#444" stroke-width="0.8"/></svg></span>
    </li>
    <li class="contact__item">teodor@scent-hub.example
      <span class="contact__icon"><svg viewBox="0 0 10 10"><rect x="1.2" y="2.5" width="7.6" height="5" fill="none" stroke="#444" stroke-width="1"/><path d="M1.2 2.5 L5 5.5 L8.8 2.5" fill="none" stroke="#444" stroke-width="1"/></svg></span>
    </li>
  </ul>

  <address class="address">
    4417 Larchmere Road<br>
    Harlow Bay, NY 11990
  </address>
</section>

<section class="card card--back">
  <div class="brand"><span class="brand__dot"></span><span>LVR, Inc.</span></div>
</section>

</body>
</html>
```